まず、縦を想定しており、画像をメインにした構成を想定しております。

上半分は覚悟を決めた中年以上の料理にが仁王立ちしているようなイメージの写真で「店を売るという選択」or「店をゆずる決断」というキャプション

下半分はやる気に満ち溢れた若者が覚悟を持って仁王立ちしているようなイメージ
「店を買う」or「店(歴史)を引きつぐ覚悟」というキャプション

そして、下の方に計算式添付の資料にあるような表を挿入。
売却した方は結局、いくら得したのか。買った方はいくら得したのかがわかるように。あとは、「査定無料」「神奈川エリアに特化した唯一のエージェントです」を記載お願いします。最後にヴェルコハーバーズという社名と連絡先を記載。

全体的なイメージではノルヴェクや外国の広告のようにシンプルだけどもどこかデザイン性を感じるように。また、信頼性も大事なので全体的にシックだけども目を引くように。
VELKO HARBORS
ヴェルコハーバーズ
0120-471-362
www.velko-harbors-jp.example
A4
片面
青系、茶系、グレー系
• 高解像度JPG (.jpg)
• イラストレーター形式 (.ai)
キャプションの修正
【メインキャプション】大事なお店、最も高く売却いたします。
【売手側キャプション】 お店を売るという選択
【買手側キャプション】お店を買うという選択

また、各キャプションを大きめに表示をお願いします。

全体的にまとまっており、柔軟に対応頂いたため。

ありがとうござました!!

```html
<!DOCTYPE html>
<html lang="ja">
<head>
<meta charset="utf-8">
<title>お店を売る・買うという選択 | VELKO HARBORS</title>
<link rel="stylesheet" href="https://fonts.googleapis.com/css2?family=Noto+Sans+JP:wght@300;400;500;700;900&family=Montserrat:wght@200;300;600&display=swap">
<style>
  :root {
    --ink: #2a2d33;
    --muted: #6b6f76;
    --paper: #ffffff;
    --photo-light: #e4e6e9;
    --photo-mid: #a9adb3;
    --photo-dark: #55595f;
    --navy: #1d3a6e;
    --navy-bright: #234a8c;
    --slate: #4c5f7a;
    --accent-red: #c8202d;
    --maroon: #7b2532;
    --rule: #c9ccd1;
    --row-alt: #f1f2f4;
  }
  * { margin: 0; padding: 0; box-sizing: border-box; }
  html, body { width: 849px; height: 1200px; overflow: hidden; background: var(--paper); }
  body { font-family: "Noto Sans JP", sans-serif; color: var(--ink); }

  .flyer { position: relative; width: 849px; height: 1200px; overflow: hidden; background: var(--paper); }

  /* hero photographs */
  .photo { position: absolute; left: 0; width: 849px; }
  .photo--sell { top: 0; height: 392px; background: linear-gradient(160deg, #f4f5f6 0%, var(--photo-light) 40%, var(--photo-mid) 100%); }
  .photo--buy { top: 445px; height: 372px; background: linear-gradient(200deg, #d3d6da 0%, var(--photo-mid) 45%, var(--photo-dark) 100%); }
  .photo svg { position: absolute; inset: 0; }

  .headline { position: absolute; font-weight: 500; line-height: 1.3; letter-spacing: 2px; }
  .headline .big { font-size: 48px; }
  .headline .key { color: var(--accent-red); font-size: 52px; font-weight: 700; }
  .headline--sell { left: 24px; top: 34px; font-size: 38px; color: var(--ink); }
  .headline--buy { left: 410px; top: 486px; font-size: 38px; color: var(--paper); text-shadow: 0 1px 6px rgba(0,0,0,.35); }

  .outline-word { position: absolute; font-family: "Montserrat", sans-serif; font-weight: 200; font-size: 72px; letter-spacing: 6px; color: transparent; -webkit-text-stroke: 1.5px var(--paper); }
  .outline-word--sell { left: 600px; top: 258px; }
  .outline-word--buy { left: 24px; top: 455px; -webkit-text-stroke-color: rgba(255,255,255,.9); }

  .tagline-band { position: absolute; left: 0; top: 392px; width: 849px; height: 53px; background: linear-gradient(90deg, var(--navy) 0%, var(--navy-bright) 100%); color: var(--paper); font-size: 29px; font-weight: 500; letter-spacing: 3px; display: flex; align-items: center; justify-content: center; }

  /* simulations */
  .simulations { position: absolute; left: 40px; top: 828px; width: 769px; height: 168px; display: flex; gap: 24px; }
  .sim { flex: 1; display: flex; flex-direction: column; }
  .sim__title { height: 22px; color: var(--paper); font-size: 12px; font-weight: 500; letter-spacing: 2px; display: flex; align-items: center; justify-content: center; }
  .sim--sell .sim__title { background: var(--slate); }
  .sim--buy .sim__title { background: var(--maroon); }
  .sim table { width: 100%; border-collapse: collapse; font-size: 11.5px; }
  .sim th, .sim td { height: 21px; border-bottom: 1px solid var(--rule); padding: 0 6px; white-space: nowrap; }
  .sim th { font-weight: 500; color: var(--muted); text-align: center; }
  .sim td { text-align: right; }
  .sim td.item { text-align: left; color: var(--ink); }
  .sim tr:nth-child(even) td { background: var(--row-alt); }
  .sim tr.total td { background: var(--photo-mid); color: var(--paper); font-weight: 700; }
  .sim__result { margin-top: auto; text-align: right; font-size: 13px; font-weight: 500; line-height: 30px; height: 30px; }
  .sim__result strong { font-size: 22px; font-weight: 900; letter-spacing: 0; }
  .sim--sell .sim__result strong { color: var(--navy); }
  .sim--buy .sim__result strong { color: var(--maroon); }

  /* footer */
  .footer { position: absolute; left: 0; top: 1008px; width: 849px; height: 192px; border-top: 2px solid var(--rule); }
  .brand-mark { position: absolute; left: 28px; top: 50px; width: 120px; text-align: center; }
  .brand-mark .square { display: block; width: 44px; height: 44px; margin: 0 auto 8px; background: var(--navy); }
  .brand-mark .name { display: block; font-size: 12px; font-weight: 700; color: var(--navy); letter-spacing: 0.5px; white-space: nowrap; }
  .contact { position: absolute; left: 172px; top: 46px; }
  .contact__lead { font-size: 14px; color: var(--muted); }
  .contact__company { font-size: 22px; font-weight: 700; color: var(--navy); margin-top: 6px; letter-spacing: 1px; }
  .contact__company span { font-size: 15px; font-weight: 500; color: var(--ink); margin-left: 8px; }
  .contact__line { display: flex; align-items: center; gap: 10px; margin-top: 8px; }
  .contact__tag { font-size: 10px; border: 1px solid var(--ink); padding: 1px 5px; }
  .contact__phone { font-size: 28px; font-weight: 700; letter-spacing: 1px; display: flex; align-items: center; gap: 6px; }
  .contact__url { font-size: 12px; color: var(--muted); margin-left: 20px; }
  .free-badge { position: absolute; left: 722px; top: 38px; width: 104px; height: 112px; background: var(--accent-red); color: var(--paper); font-size: 26px; font-weight: 900; line-height: 1.2; display: flex; align-items: center; justify-content: center; text-align: center; letter-spacing: 6px; }
</style>
</head>
<body>
<main class="flyer">

  <section class="photo photo--sell" role="img" aria-label="厨房で腕を組んで立つ年配のシェフのモノクロ写真">
    <svg width="849" height="392" viewBox="0 0 849 392" aria-hidden="true">
      <polygon points="0,250 849,170 849,392 0,392" fill="#7d8187" opacity="0.55"/>
      <polygon points="520,0 849,0 849,392 700,392" fill="#8f9399" opacity="0.35"/>
    </svg>
  </section>
  <h2 class="headline headline--sell"><span class="big">お店を<span class="key">売</span>る</span><br>という選択</h2>
  <div class="outline-word outline-word--sell">SELL</div>

  <p class="tagline-band">大事なお店、最も高く売却いたします。</p>

  <section class="photo photo--buy" role="img" aria-label="業務用厨房で腕を組んで立つ若いシェフのモノクロ写真">
    <svg width="849" height="372" viewBox="0 0 849 372" aria-hidden="true">
      <polygon points="0,0 360,0 220,372 0,372" fill="#c6c9cd" opacity="0.45"/>
      <polygon points="620,0 849,0 849,372 560,372" fill="#3f4348" opacity="0.35"/>
    </svg>
  </section>
  <div class="outline-word outline-word--buy">BUY</div>
  <h2 class="headline headline--buy"><span class="big">お店を<span class="key">買</span>う</span><br>という選択</h2>

  <section class="simulations">
    <div class="sim sim--sell">
      <h3 class="sim__title">売店コストシミュレーション</h3>
      <table>
        <tr><th></th><th>通常売店</th><th>弊社サービス</th></tr>
        <tr><td class="item">解約前手数料</td><td>▲450,000円</td><td>0円</td></tr>
        <tr><td class="item">内装解体費用</td><td>▲550,000円</td><td>0円</td></tr>
        <tr><td class="item">造作売買代金</td><td>0円</td><td>2,000,000円</td></tr>
        <tr class="total"><td class="item">計</td><td>▲1,000,000円</td><td>2,000,000円</td></tr>
      </table>
      <p class="sim__result"><strong>3,000,000</strong>円のメリット</p>
    </div>
    <div class="sim sim--buy">
      <h3 class="sim__title">出店コストシミュレーション</h3>
      <table>
        <tr><th></th><th>通常出店</th><th>弊社サービス</th></tr>
        <tr><td class="item">内装設備投資額</td><td>13,000,000円</td><td>0円</td></tr>
        <tr><td class="item">造作売買代金</td><td>0円</td><td>3,500,000円</td></tr>
        <tr class="total"><td class="item">計</td><td>13,000,000円</td><td>3,500,000円</td></tr>
      </table>
      <p class="sim__result"><strong>9,500,000</strong>円のコストダウン</p>
    </div>
  </section>

  <footer class="footer">
    <div class="brand-mark">
      <span class="square"></span>
      <span class="name">VELKO HARBORS</span>
    </div>
    <div class="contact">
      <p class="contact__lead">神奈川エリアに特化した唯一のエージェントです。</p>
      <p class="contact__company">VELKO HARBORS<span>ヴェルコハーバーズ</span></p>
      <div class="contact__line">
        <span class="contact__tag">お問合せ</span>
        <span class="contact__phone">
          <svg width="22" height="22" viewBox="0 0 24 24" aria-hidden="true"><path fill="#2a2d33" d="M6.6 10.8a15.1 15.1 0 0 0 6.6 6.6l2.2-2.2a1 1 0 0 1 1-.25 11.4 11.4 0 0 0 3.6.6 1 1 0 0 1 1 1V20a1 1 0 0 1-1 1A17 17 0 0 1 3 4a1 1 0 0 1 1-1h3.5a1 1 0 0 1 1 1c0 1.25.2 2.45.6 3.6a1 1 0 0 1-.25 1z"/></svg>
          0120-471-362
        </span>
        <span class="contact__url">www.velko-harbors-jp.example</span>
      </div>
    </div>
    <div class="free-badge">無料<br>査定<br>実施中</div>
  </footer>

</main>
</body>
</html>
```